Online medical reviews website needs banner advert!

We need banner advert templates for our website, www.traineepanel.net. These should meet the technical requirements of our partner (uploaded).

Our groundbreaking website allows doctors in training to rate and review their training.

The adverts should use the same modern design language and colour scheme as our website. They should use the text 'Help a junior doctor make a big decision - rate your training!'.

Vector assets should be supplied, allowing us to use alternative text in future.
Updates

Industry/Entity Type

Healthcare

Font styles to use
Other font styles liked:
• Karla

Colors
3277b5
0555a3
ffffff

Requirements
Must have
• Similar design to our website. Should be elegant & modern. Must allow future text to be easily inserted.
Should not have
• Unrelated design.

```html
<!DOCTYPE html>
<html lang="en">
<head>
<meta charset="utf-8">
<title>Trainee Panel – Banner Set</title>
<link href="https://fonts.googleapis.com/css2?family=Karla:wght@400;500;600;700&display=swap" rel="stylesheet">
<style>
  :root {
    --brand-blue: #0555a3;
    --brand-light: #3277b5;
    --cta-blue: #1a7df0;
    --white: #ffffff;
    --canvas: #f2f2f2;
    --photo-dark: #1f3150;
    --photo-mid: #3a4a5e;
    --photo-green: #2f4a32;
    --muted: #9aa3ad;
  }
  * { box-sizing: border-box; margin: 0; padding: 0; }
  html, body {
    width: 1200px; height: 800px; overflow: hidden;
    background: var(--canvas);
    font-family: "Karla", Arial, sans-serif;
  }
  .canvas { position: relative; width: 1200px; height: 800px; }

  .ad { position: absolute; overflow: hidden; background: var(--white);
        box-shadow: 0 8px 10px -4px rgba(0,0,0,0.35); }

  .brand-name { color: var(--white); font-weight: 400; letter-spacing: -0.3px; white-space: nowrap; }

  .photo {
    position: absolute;
    background:
      linear-gradient(180deg, rgba(5,40,90,0.55) 0%, rgba(20,40,70,0.55) 55%, rgba(30,60,40,0.6) 100%),
      linear-gradient(90deg, var(--photo-mid), var(--photo-dark) 50%, var(--photo-mid));
  }

  .headline { color: var(--white); font-weight: 600; text-transform: uppercase;
              text-align: center; letter-spacing: 0.6px; line-height: 1.25; }

  .cta { position: absolute; background: var(--cta-blue); color: var(--white);
         font-weight: 700; display: flex; align-items: center; justify-content: center;
         border-bottom: 2px solid #0c5fc4; letter-spacing: 0.3px; }

  .url { color: var(--white); font-weight: 400; letter-spacing: 0.4px; }

  /* Skyscraper */
  .skyscraper { left: 65.6px; top: 160px; width: 240px; height: 480px; }
  .skyscraper .header { position: absolute; top: 0; left: 0; width: 240px; height: 60px;
                        background: var(--brand-blue); display: flex; align-items: center; justify-content: center; }
  .skyscraper .header .brand-name { font-size: 24px; }
  .skyscraper .photo { top: 72px; left: 0; width: 240px; height: 336px; }
  .skyscraper .headline { position: absolute; top: 116px; width: 100%; font-size: 18.5px; line-height: 25.6px; }
  .skyscraper .cta { left: 42px; top: 264px; width: 155px; height: 30px; font-size: 13px; }
  .skyscraper .footer { position: absolute; bottom: 0; left: 0; width: 240px; height: 60px;
                        background: var(--brand-blue); display: flex; align-items: center; justify-content: center; }
  .skyscraper .url { font-size: 12px; }

  /* Leaderboards */
  .leaderboard { left: 358.4px; top: 160px; width: 776px; height: 72px; }
  .banner { left: 358.4px; top: 293.6px; width: 582.4px; height: 72px; }
  .leaderboard .photo, .banner .photo { top: 0; left: 170px; right: 0; height: 72px; }
  .shapes { position: absolute; top: 0; left: 0; }
  .strip-logo { position: absolute; left: 18px; top: 18px; }
  .strip-logo .brand-name { font-size: 20px; }
  .strip-headline { position: absolute; left: 200px; top: 20px; width: 200px; font-size: 13px; line-height: 16px; }
  .strip-cta { left: 422px; top: 25.6px; width: 136px; height: 22.4px; font-size: 10.5px; }
  .strip-url { position: absolute; left: 614px; width: 162px; top: 10px; height: 62px;
               display: flex; align-items: center; justify-content: center; font-size: 11.5px; }
  .strip-url-small { position: absolute; left: 16px; top: 60px; font-size: 9px; color: var(--muted); letter-spacing: 0.5px; }

  /* Medium rectangle */
  .rectangle { left: 358.4px; top: 428px; width: 240px; height: 212px; }
  .rectangle .header { position: absolute; top: 0; left: 0; width: 240px; height: 48px;
                       background: var(--brand-blue); display: flex; align-items: center; justify-content: center; }
  .rectangle .header .brand-name { font-size: 20px; }
  .rectangle .photo { top: 54.4px; left: 0; width: 240px; height: 117.6px; }
  .rectangle .headline { position: absolute; top: 24px; width: 100%; font-size: 12.5px; line-height: 16px; }
  .rectangle .cta { left: 52px; top: 81px; width: 136px; height: 25px; font-size: 10.5px; }
  .rectangle .footer { position: absolute; bottom: 0; left: 0; width: 240px; height: 33.6px;
                       background: var(--brand-blue); display: flex; align-items: center; justify-content: center; }
  .rectangle .url { font-size: 12px; }
</style>
</head>
<body>
<div class="canvas">

  <section class="ad skyscraper">
    <div class="header"><span class="brand-name">Trainee Panel</span></div>
    <div class="photo" role="img" aria-label="Photo of a grand college building with a fountain and lawn, tinted blue">
      <p class="headline">Help a junior<br>doctor make<br>a big decision</p>
      <div class="cta">Rate your training!</div>
    </div>
    <div class="footer"><span class="url">www.traineepanel.net</span></div>
  </section>

  <section class="ad leaderboard">
    <div class="photo" role="img" aria-label="Photo of a college building facade, tinted blue">
      <p class="headline strip-headline" style="left:30px">Help a junior doctor make<br>a big decision</p>
      <div class="cta strip-cta" style="left:252px">Rate your training!</div>
    </div>
    <svg class="shapes" width="776" height="72" viewBox="0 0 776 72">
      <polygon points="0,0 190,0 171,72 0,72" fill="var(--white)"/>
      <polygon points="0,0 190,0 174,60 0,60" fill="var(--brand-blue)"/>
      <polygon points="596,0 776,0 776,72 574,72" fill="var(--white)"/>
      <polygon points="612,10 776,10 776,72 586,72" fill="var(--brand-blue)"/>
    </svg>
    <div class="strip-logo"><span class="brand-name">Trainee Panel</span></div>
    <div class="strip-url"><span class="url">www.traineepanel.net</span></div>
  </section>

  <section class="ad banner">
    <div class="photo" role="img" aria-label="Photo of a college building facade, tinted blue">
      <p class="headline strip-headline" style="left:30px">Help a junior doctor make<br>a big decision</p>
      <div class="cta strip-cta" style="left:252px">Rate your training!</div>
    </div>
    <svg class="shapes" width="582.4" height="72" viewBox="0 0 582.4 72">
      <polygon points="0,0 190,0 171,72 0,72" fill="var(--white)"/>
      <polygon points="0,0 190,0 174,60 0,60" fill="var(--brand-blue)"/>
    </svg>
    <div class="strip-logo"><span class="brand-name">Trainee Panel</span></div>
    <span class="strip-url-small">www.traineepanel.net</span>
  </section>

  <section class="ad rectangle">
    <div class="header"><span class="brand-name">Trainee Panel</span></div>
    <div class="photo" role="img" aria-label="Photo of a college building facade, tinted blue">
      <p class="headline">Help a junior doctor make<br>a big decision</p>
      <div class="cta">Rate your training!</div>
    </div>
    <div class="footer"><span class="url">www.traineepanel.net</span></div>
  </section>

</div>
</body>
</html>
```